Business Card Design for Occupational Medicine Start Up Company

We need to design a professional business card. We are a healthcare company providing occupational medicine services to blue collar industries. We are professional, efficient and high quality service providers.

Target Market(s)

Blue Collar Industry: Shipbuilding, Ports, Trucking Companies; The Executives and Safety Officers for these companies

Industry/Entity Type

Healthcare

Contact Information for Business Card

Logo, Name, Title, Email, Phone

Other font styles liked:
• Please match our Brand Guide

Requirements
Must have
• Our Company Colors and Logo

```html
<!DOCTYPE html>
<html lang="en">
<head>
<meta charset="utf-8">
<title>Crewline Health — Business Card</title>
<link rel="stylesheet" href="https://fonts.googleapis.com/css2?family=Montserrat:wght@700&family=Arimo:wght@400&display=swap">
<style>
  :root {
    --navy: #1b2a80;
    --navy-deep: #172372;
    --sky: #3aa6e4;
    --gold: #f3b840;
    --paper: #ffffff;
    --ink: #1b1b1b;
    --rule: #dcdde3;
    --backdrop: #d9d9d9;
  }
  * { box-sizing: border-box; margin: 0; padding: 0; }
  html, body { width: 1200px; height: 900px; overflow: hidden; }
  body {
    background: var(--backdrop);
    position: relative;
    font-family: "Arimo", Arial, sans-serif;
  }
  .card {
    position: absolute;
    width: 560px;
    height: 320px;
    box-shadow: 0 6px 18px rgba(0,0,0,0.18);
  }
  .card-front {
    left: 190px; top: 100px;
    background: var(--navy-deep);
    display: flex; align-items: center; justify-content: center;
  }
  .card-back {
    left: 450px; top: 480px;
    background: var(--paper);
  }
  .brand {
    display: flex; align-items: center; gap: 12px;
    font-family: "Montserrat", Arial, sans-serif;
    font-weight: 700;
    letter-spacing: 0.5px;
    text-transform: uppercase;
  }
  .brand-dot { width: 18px; height: 18px; border-radius: 50%; }
  .card-front .brand { color: var(--paper); font-size: 30px; }
  .card-front .brand-dot { background: var(--gold); }
  .card-back .brand {
    position: absolute; left: 34px; top: 44px;
    color: var(--navy); font-size: 22px;
  }
  .card-back .brand-dot { background: var(--gold); width: 14px; height: 14px; }
  .holder {
    position: absolute; right: 34px; top: 40px;
    text-align: right;
  }
  .holder-name {
    font-family: "Montserrat", Arial, sans-serif;
    font-weight: 700; font-size: 22px; color: var(--navy);
  }
  .holder-title { font-size: 11px; color: var(--ink); margin-top: 2px; }
  .divider {
    position: absolute; left: 34px; right: 34px; top: 112px;
    height: 1px; background: var(--rule);
  }
  .contacts {
    position: absolute; left: 34px; bottom: 46px;
    list-style: none; font-size: 14px; color: var(--ink);
  }
  .contacts li { display: flex; align-items: center; gap: 14px; margin-top: 8px; }
  .contacts svg { width: 14px; height: 14px; fill: var(--navy); }
  .accent {
    position: absolute; right: 0; bottom: 54px;
    width: 230px; height: 100px;
    border-radius: 50px 0 0 50px;
    background: linear-gradient(180deg, var(--gold) 0%, var(--navy) 50%, var(--sky) 100%);
  }
</style>
</head>
<body>
  <section class="card card-front">
    <div class="brand"><span class="brand-dot"></span>Crewline Health</div>
  </section>

  <section class="card card-back">
    <div class="brand"><span class="brand-dot"></span>Crewline Health</div>
    <div class="holder">
      <div class="holder-name">Marisol Teague</div>
      <div class="holder-title">Manager</div>
    </div>
    <div class="divider"></div>
    <ul class="contacts">
      <li>
        <svg viewBox="0 0 24 24" aria-hidden="true"><path d="M6.6 10.8a15 15 0 0 0 6.6 6.6l2.2-2.2a1 1 0 0 1 1-.25 11.4 11.4 0 0 0 3.6.57 1 1 0 0 1 1 1V20a1 1 0 0 1-1 1A17 17 0 0 1 3 4a1 1 0 0 1 1-1h3.5a1 1 0 0 1 1 1c0 1.25.2 2.45.57 3.57a1 1 0 0 1-.25 1z"/></svg>
        555 210 4387
      </li>
      <li>
        <svg viewBox="0 0 24 24" aria-hidden="true"><path d="M2 5h20v14H2z M2 5l10 8 10-8" fill="none" stroke="#1b2a80" stroke-width="2"/></svg>
        hello@crewlinehealth.com
      </li>
    </ul>
    <div class="accent" role="img" aria-label="Brand accent graphic in gold, navy and sky blue bands"></div>
  </section>
</body>
</html>
```